Stationery design bilingual preschool
Meadowlark preschool
Stationery design bilingual preschool - Childcare
Creative Brief
Bright & Fun-filled
Marita Sundqvist
Preschool director
Lövhagsvägen 9 128 31 Skarpnäck Sweden
angsfagelforskolan@postlada.se
www.angsfagelforskolan.com
Back of the business card suppose to have the same information as the front side but on Swedish.
(Subtitle) Ängsfågel Förskola AB ( name) Marita Sundqvist (title) Förskolechef (address) Lövhagsvägen 9 128 31 Skarpnäck (phone) Tel. 08 731 94 62 (cell) Mob. 073 862 40 15 (email) angsfagelforskolan@postlada.com (web side) www.angsfagelforskolan. com
butterfly2004 butterfly2004
Dear designers, I'd like to see design drafts ideas for the following products: 1. Business card 2. Letterhead 3. Envelope 4. Folder 5. CD and CD cover 6. Email signature 7. Presentation 8.Thank you card 8. Stamp 9. T-shirt, Hoody, Winter jacket/ Rain jacket, Cap, Scarf 10. Pen 11. Meadowlark character toy Thank you, PH

```html
<!DOCTYPE html>
<html lang="en">
<head>
<meta charset="utf-8">
<title>Meadowlark preschool – Business card</title>
<link href="https://fonts.googleapis.com/css2?family=Open+Sans:wght@400;600;700;800&display=swap" rel="stylesheet">
<style>
  :root{
    --backdrop:#4a4a4c;
    --card-white:#ffffff;
    --card-shade:#eeeeee;
    --orange-light:#ffb02e;
    --orange-deep:#ee6a0a;
    --green:#3f9a1c;
    --green-dark:#2f7d12;
    --lime:#9ccc2a;
    --text:#555555;
    --muted:#8a8a8a;
  }
  *{box-sizing:border-box;margin:0;padding:0}
  html,body{width:1200px;height:871px;overflow:hidden}
  body{
    background:var(--backdrop);
    font-family:"Open Sans",Arial,sans-serif;
    display:flex;flex-direction:column;align-items:center;justify-content:center;gap:56px;
  }
  .card{
    width:620px;height:354px;border-radius:18px;position:relative;overflow:hidden;
    box-shadow:0 10px 28px rgba(0,0,0,.35);
  }
  /* back side */
  .card-back{
    background:radial-gradient(ellipse at 50% 45%,var(--orange-light) 0%,#f99a1c 45%,var(--orange-deep) 100%);
    display:flex;flex-direction:column;align-items:center;justify-content:center;
  }
  .card-back .brand-name{font-size:46px;font-weight:800;color:var(--green-dark);line-height:1.05;text-align:center}
  .card-back .brand-sub{margin-top:10px;font-size:15px;font-weight:600;color:#fff3dc;letter-spacing:.5px}
  /* front side */
  .card-front{background:linear-gradient(180deg,var(--card-white) 0%,var(--card-shade) 100%)}
  .brand-block{
    position:absolute;left:30px;top:78px;width:230px;
    display:flex;align-items:center;gap:12px;
  }
  .brand-dot{width:46px;height:46px;border-radius:50%;background:var(--orange-light);flex:none}
  .brand-block .brand-name{font-size:28px;font-weight:800;color:var(--green);line-height:1.05}
  .divider{position:absolute;left:282px;top:48px;width:1px;height:190px;background:#cfcfcf}
  .contact{position:absolute;left:306px;top:52px;width:290px;color:var(--text)}
  .person{font-size:23px;font-weight:700;color:var(--green)}
  .role{font-size:14px;font-weight:600;color:var(--orange-deep);margin-bottom:20px}
  .address{font-size:13px;line-height:1.45;margin-bottom:10px}
  .line{display:flex;align-items:center;gap:9px;font-size:13px;line-height:1.75}
  .line svg{width:14px;height:14px;flex:none}
  .lime-stripe{position:absolute;left:0;right:0;bottom:52px;height:8px;background:var(--lime)}
  .web-band{
    position:absolute;left:0;right:0;bottom:0;height:52px;background:var(--green);
    display:flex;align-items:center;padding-left:30px;
    color:#fff;font-size:17px;font-weight:600;letter-spacing:.3px;
  }
  .corner-dot{position:absolute;right:24px;bottom:10px;width:34px;height:34px;border-radius:50%;background:var(--orange-light)}
</style>
</head>
<body>
  <section class="card card-back">
    <p class="brand-name">Meadowlark<br>preschool</p>
    <p class="brand-sub">Ängsfågel Förskola AB</p>
  </section>

  <section class="card card-front">
    <div class="brand-block">
      <span class="brand-dot"></span>
      <p class="brand-name">Meadowlark preschool</p>
    </div>
    <div class="divider"></div>
    <div class="contact">
      <p class="person">Marita Sundqvist</p>
      <p class="role">Preschool director</p>
      <p class="address">Lövhagsvägen 9<br>128 31 Skarpnäck, Sweden</p>
      <p class="line">
        <svg viewBox="0 0 16 16"><path fill="#3f9a1c" d="M3.5 1.5l2.5 0 1.2 3.2-1.6 1.2a8 8 0 0 0 4.5 4.5l1.2-1.6 3.2 1.2v2.5c0 .8-.7 1.5-1.5 1.5A12 12 0 0 1 2 3c0-.8.7-1.5 1.5-1.5z"/></svg>
        +46 8 731 94 62
      </p>
      <p class="line">
        <svg viewBox="0 0 16 16"><rect x="4" y="1" width="8" height="14" rx="1.5" fill="#3f9a1c"/><rect x="5.5" y="3" width="5" height="8" fill="#fff"/></svg>
        +46 73 862 40 15
      </p>
      <p class="line">
        <svg viewBox="0 0 16 16"><rect x="1" y="3" width="14" height="10" rx="1" fill="#3f9a1c"/><path d="M1.5 3.5L8 9l6.5-5.5" stroke="#fff" stroke-width="1.3" fill="none"/></svg>
        angsfagelforskolan@postlada.se
      </p>
    </div>
    <div class="lime-stripe"></div>
    <div class="web-band">www.angsfagelforskolan.com</div>
    <span class="corner-dot"></span>
  </section>
</body>
</html>
```